The Velorind Project

All information regarding the design is located at Velorind.com. Any questions regarding the project, will be answered on the site.

```html
<!DOCTYPE html>
<html lang="en">
<head>
<meta charset="utf-8">
<title>Velorind</title>
<link rel="stylesheet" href="https://fonts.googleapis.com/css2?family=PT+Sans:wght@400;700&family=Gelasio:wght@400&display=swap">
<style>
  :root {
    --bar-dark: #2b2b2b;
    --bar-top: #3c3c3c;
    --nav-divider: #1a1a1a;
    --nav-divider-light: #4a4a4a;
    --nav-text: #ffffff;
    --login-green: #a8d88a;
    --login-green-dark: #8fc66e;
    --login-text: #2e4a1f;
    --page-bg: #efefef;
    --logo-ink: #1c1c1c;
    --field-border: #8cc767;
    --field-bg: #ffffff;
    --placeholder: #7a7a7a;
    --icon-fill: #2a1f22;
    --footer-bg: #e6e6e6;
    --footer-line: #d2d2d2;
    --footer-text: #5a5a5a;
  }
  * { box-sizing: border-box; margin: 0; padding: 0; }
  html, body { width: 1200px; height: 923px; overflow: hidden; }
  body {
    position: relative;
    background: var(--page-bg);
    font-family: "PT Sans", sans-serif;
  }
  .top-bar {
    position: absolute; left: 0; top: 0; width: 1200px; height: 34px;
    background: linear-gradient(var(--bar-top), var(--bar-dark));
    display: flex; justify-content: space-between;
  }
  .main-nav { display: flex; list-style: none; }
  .main-nav li {
    height: 34px; line-height: 34px;
    font-size: 13px; font-weight: 700; color: var(--nav-text);
    border-right: 1px solid var(--nav-divider);
    box-shadow: 1px 0 0 var(--nav-divider-light);
    text-transform: uppercase;
  }
  .main-nav li:nth-child(1) { width: 64px; padding-left: 18px; }
  .main-nav li:nth-child(2) { width: 86px; padding-left: 20px; }
  .main-nav li:nth-child(3) { width: 80px; padding-left: 21px; }
  .main-nav li:nth-child(4) { width: 76px; padding-left: 20px; }
  .main-nav li:nth-child(5) { width: 75px; padding-left: 20px; }
  .main-nav li:nth-child(6) { width: 69px; padding-left: 20px; }
  .main-nav li:nth-child(7) { width: 82px; padding-left: 19px; }
  .caret { display: inline-block; margin-left: 5px; vertical-align: 2px; }
  .login-button {
    width: 80px; height: 34px; line-height: 34px; text-align: center;
    background: linear-gradient(var(--login-green), var(--login-green-dark));
    color: var(--login-text); font-size: 15px; font-weight: 700;
  }
  .brand-name {
    position: absolute; left: 0; top: 140px; width: 1200px; text-align: center;
    font-family: "Gelasio", serif; font-size: 70px; font-weight: 400;
    color: var(--logo-ink); letter-spacing: -1.5px;
  }
  .search-form {
    position: absolute; left: 373px; top: 255px; width: 476px; height: 69px;
    border: 2px solid var(--field-border); border-radius: 3px;
    background: var(--field-bg);
    box-shadow: 4px 5px 5px rgba(0,0,0,0.35);
    display: flex;
  }
  .search-field {
    flex: 1; border-right: 2px solid var(--field-border);
    padding: 18px 0 0 13px;
    font-size: 23px; color: var(--placeholder);
  }
  .search-button {
    width: 78px; display: flex; align-items: center; justify-content: center;
  }
  .search-icon {
    width: 60px; height: 56px; border-radius: 8px;
    background: radial-gradient(circle at 50% 60%, var(--icon-fill) 45%, rgba(42,31,34,0.15) 72%);
  }
  .site-footer {
    position: absolute; left: 0; top: 889px; width: 1200px; height: 34px;
    background: var(--footer-bg); border-top: 1px solid var(--footer-line);
    text-align: right; padding-right: 14px; line-height: 34px;
    font-size: 10px; font-weight: 700; color: var(--footer-text); letter-spacing: 0.5px;
  }
</style>
</head>
<body>
  <header class="top-bar">
    <ul class="main-nav">
      <li>Web</li>
      <li>Images</li>
      <li>Video</li>
      <li>News</li>
      <li>Maps</li>
      <li>Mail</li>
      <li>More<svg class="caret" width="8" height="5" viewBox="0 0 8 5"><path d="M0 0h8L4 5z" fill="#ffffff"/></svg></li>
    </ul>
    <div class="login-button">LOG IN</div>
  </header>

  <h1 class="brand-name">Velorind</h1>

  <div class="search-form">
    <div class="search-field">Write your question here</div>
    <div class="search-button">
      <div class="search-icon" role="img" aria-label="Search button icon"></div>
    </div>
  </div>

  <footer class="site-footer">© 2012 VELORIND. ALL RIGHTS RESERVED.</footer>
</body>
</html>
```